Flyer-Design für Karin Dossow
Zielgruppe
Ich bin psychologische Beraterin und Heilpraktikerin für Psychotherapie. Ich biete ein Coaching speziell für Mütter (meist Mütter mit neugeborenen Babys) an. Dieses Mütter-Coaching will ich bewerben. Die Flyer werden unter anderen an Ärzte und Hebammen weiter gegeben und dort in den Praxen ausliegen.
Aufgabenstellung
In meinem Logo herrschen die Farben orange und grau vor - es wäre schön, wenn sich diese Farben im Flyer wiederfinden würden - evtl. kombiniert mit mittelblau oder einem hellem grün.
Des weiteren möchte ich später Flyer im Din Lang Format (einseitig) mit anderen Angeboten erstellen. Das sollte mit dem Design dann auch möglich sein.
Der Schrifttyp soll bitte Arial sein, passend zum Logo. Ich habe bei Bildarko Fotos zu dem Thema erstanden, die ich stimmig finde. Diese Bilder sollten im Flyer genutzt werden.
Für diesen Flyer hätte ich gerne das Format: Falzblatt mit Wickelfalz - 279 x 219 mm

```html
<!DOCTYPE html>
<html lang="de">
<head>
<meta charset="utf-8">
<title>Falzblatt Coaching für Mütter – Karin Dossow</title>
<link href="https://fonts.googleapis.com/css2?family=Arimo:wght@400;700&family=Roboto+Condensed:wght@400;500&display=swap" rel="stylesheet">
<style>
:root{
  --bg:#9dbedb;
  --orange:#f09d33;
  --orange-light:#f5b04b;
  --orange-band:#f3a23a;
  --accent:#ec9a2c;
  --grey-text:#555;
  --grey-dark:#444;
  --panel-grey:#f1efed;
  --white:#fff;
  --photo-a:#d9c7b8;
  --photo-b:#4a3c38;
}
*{box-sizing:border-box;margin:0;padding:0}
html,body{width:1200px;height:900px;overflow:hidden}
body{background:var(--bg);font-family:"Arimo",Arial,sans-serif;color:var(--grey-text);position:relative}
.spread{position:absolute;top:250px;width:561px;height:400px;background:var(--white)}
.spread--outside{left:31px}
.spread--inside{left:608px}
.panel{position:absolute;top:0;bottom:7px;overflow:hidden}
.p1{left:0;width:184px}.p2{left:184px;width:188px}.p3{left:372px;width:189px}
.band-bottom{position:absolute;left:0;right:0;bottom:0;height:7px;background:var(--orange-band)}
.block{position:absolute;left:0;right:0}
.block--orange{background:var(--orange)}
.block--light{background:var(--orange-light)}
.pointer::after{content:"";position:absolute;left:50%;bottom:-6px;margin-left:-6px;border-left:6px solid transparent;border-right:6px solid transparent;border-top:6px solid var(--orange)}
.block--light.pointer::after{border-top-color:var(--orange-light)}
.pointer-up::before{content:"";position:absolute;left:50%;top:-6px;margin-left:-6px;border-left:6px solid transparent;border-right:6px solid transparent;border-bottom:6px solid var(--orange-light)}
.center{text-align:center}
.lead{color:var(--white);font-weight:700;font-size:11px;line-height:16px;padding-top:20px}
.quote{color:var(--white);font-weight:700;font-size:13px;line-height:16px;padding:28px 10px 0}
.brand{font-size:15px;color:var(--accent);letter-spacing:.2px;line-height:18px}
.tag{font-size:9.5px;line-height:12px;color:#777}
.tag strong{font-weight:700;color:var(--accent)}
.block--light .tag strong,.block--light .tag{color:#b85f10}
.body{font-size:6.9px;line-height:10.5px;color:var(--grey-text)}
.body p{margin-bottom:10px}
.contact{font-size:7.2px;line-height:10.6px;color:var(--grey-dark)}
.contact .name{font-size:9px;line-height:12px}
.contact p{margin-bottom:9px}
.services{color:var(--white);font-size:6.9px;line-height:12px;font-weight:700}
.services h3{font-size:8.5px;line-height:14px;color:#b85f10;font-weight:700;margin-bottom:1px}
.services li{list-style:none;color:#fff6e6}
.photo{position:absolute;left:0;right:0}
.photo--mother{background:linear-gradient(135deg,var(--photo-a),#c9a894 50%,var(--photo-b))}
.photo--tired{background:linear-gradient(90deg,#eeeae6 0%,#b8aaa2 45%,#5c6170 100%)}
.band-top{position:absolute;left:0;right:0;top:0;height:7px;background:var(--orange-band)}
.marker{position:absolute;top:7px;width:0;height:0;border-left:5px solid transparent;border-right:5px solid transparent;border-top:5px solid var(--orange-band)}
.p-grey{background:var(--panel-grey)}
.h-col{font-family:"Roboto Condensed",Arial,sans-serif;font-size:8.5px;letter-spacing:.6px;color:var(--grey-dark);font-weight:500}
.h-col span{color:var(--accent)}
.rule{width:20px;height:1px;background:var(--grey-dark);margin:4px 0 0}
.rule.mid{margin:4px auto 0}
.sub{font-family:"Roboto Condensed",Arial,sans-serif;font-size:7.5px;letter-spacing:.6px;color:var(--grey-dark);margin-bottom:6px}
.bullets li{list-style:none;font-size:6.6px;line-height:10px;margin-bottom:9px;color:var(--grey-text)}
.bullets li::before{content:"\2022\00a0";color:var(--accent)}
.offer{font-size:6.6px;line-height:10.5px}
.offer h4{font-size:7.5px;color:var(--accent);font-weight:400;display:flex;align-items:center;gap:4px;margin-bottom:4px}
.plus{width:8px;height:8px;border-radius:50%;background:var(--grey-dark);color:#fff;font-size:7px;line-height:8px;text-align:center;font-weight:700}
.offer p{margin-bottom:13px}
</style>
</head>
<body>

<section class="spread spread--outside" aria-label="Außenseite">
  <div class="panel p1">
    <div class="block block--orange pointer center lead" style="top:0;height:96px">Warum Coaching<br>extra für Mütter?<br>Nur wer gut für sich selbst sorgt,<br>kann auch für andere da sein!</div>
    <div class="block center" style="top:110px">
      <div class="brand">karindossow</div>
      <div class="tag" style="margin-top:6px"><strong>Coaching für Mütter</strong><br>Begleitung - Stärkung - Beratung</div>
    </div>
    <div class="block body" style="top:176px;padding:0 8px">
      <p>Als geprüfte psychologische Beraterin und Heilpraktikerin für Psychotherapie habe ich mich besonders auf das Coaching für Mütter spezialisiert.</p>
      <p>Ich setze dabei die Methode des lösungsorientierten Kurzzeitcoachings ein, das den Fokus auf Stärken und Lösungen und nicht die Probleme und Hindernisse in den Vordergrund stellt.</p>
      <p>Das Konzept wird durch Achtsamkeits- und Entspannungsübungen abgerundet. Aspekte der „gewaltfreien“ = wertschätzenden Kommunikation werden für individuelle Konfliktlösungen im familiären Alltag genutzt.</p>
      <p>Starten Sie mit einem neuen und liebevollen Blick auf Ihr Leben und auf Ihre Fähigkeiten.</p>
      <p>Sie werden erstaunt sein, was alles in Ihnen wohnt.</p>
    </div>
  </div>

  <div class="panel p2">
    <div class="block block--light pointer center" style="top:0;height:96px;padding-top:24px">
      <div class="brand" style="color:#9a5a1c">karindossow</div>
      <div class="tag" style="margin-top:8px"><strong>Coaching für Mütter</strong><br>Begleitung - Stärkung - Beratung</div>
    </div>
    <div class="block center contact" style="top:130px">
      <p><span class="name">Karin Dossow</span><br>Heilpraktikerin für Psychotherapie<br>Geprüfte Psychologische Beraterin</p>
      <p>Telefon: 0160 412 38 605<br>Email: info@karin-dossow.de<br>www.karin-dossow.de</p>
      <p>Praxisgemeinschaft am Hain<br>Falkenweg 18c<br>41470 Neuss am Rhein</p>
    </div>
    <div class="block block--light pointer-up center services" style="top:290px;bottom:0;padding-top:14px">
      <h3>Weiteres Leistungsspektrum</h3>
      <ul>
        <li>Psychologische Beratung</li>
        <li>Stressbewältigung – Burnoutprävention</li>
        <li>Achtsamkeitstraining – Atemfluss-Methode</li>
        <li>Lösungsfokussierte Kurzzeittherapie</li>
        <li>Kommunikation im Alltag (nach GfK)</li>
        <li>Energiearbeit – Geistiges Heilen</li>
      </ul>
    </div>
  </div>

  <div class="panel p3">
    <div class="block block--orange pointer center quote" style="top:0;height:96px">„Das Baby ist da<br>und nichts ist mehr<br>wie es war“</div>
    <div class="photo photo--mother" style="top:96px;height:194px" role="img" aria-label="Foto: Mutter hält ihr schlafendes Neugeborenes an der Schulter"></div>
    <div class="block center" style="top:318px">
      <div class="brand">karindossow</div>
      <div class="tag" style="margin-top:6px"><strong>Coaching für Mütter</strong><br>Begleitung - Stärkung - Beratung</div>
    </div>
  </div>
  <div class="band-bottom"></div>
</section>

<section class="spread spread--inside" aria-label="Innenseite">
  <div class="panel p1 p-grey">
    <div class="block" style="top:20px;padding:0 14px">
      <div class="h-col">IHRE <span>SITUATION</span></div>
    </div>
    <ul class="block bullets" style="top:40px;padding:0 10px 0 14px">
      <li>Haben Sie sich Ihr Mutterglück anders vorgestellt? - Sie hatten sich so auf Ihr Baby gefreut, aber die Realität ist gar nicht so, wie Sie sie sich das gedacht haben?</li>
      <li>Oder Sie haben bereits ein oder mehrere Kinder aber trotzdem ist jetzt alles anders?</li>
      <li>Fühlen Sie sich allein, isoliert: Ihre Kollegen und Freunde führen weiterhin Ihr früheres Leben - Sie sind aber nicht mehr mit dabei?</li>
      <li>Das Verständnis Ihrer Umgebung für Ihre neue Situation fehlt. Sogar die Partnerschaft ist plötzlich ganz anders als sie es vorher war?</li>
      <li>Sie werden nur noch als Mutter wahrgenommen - kaum mehr als die Frau und die Persönlichkeit, die Sie vorher waren und auch immer noch sind?</li>
      <li>Sie fühlen sich oft erschöpft, ratlos, überfordert, unverstanden?</li>
    </ul>
    <div class="photo photo--tired" style="top:280px;bottom:0" role="img" aria-label="Foto: erschöpfte Mutter mit Baby im Arm neben dem Kinderbett"></div>
  </div>

  <div class="panel p2">
    <div class="block center" style="top:20px">
      <div class="h-col">MEINE <span>UNTERSTÜTZUNG</span></div><div class="rule mid"></div>
    </div>
    <div class="block center offer" style="top:50px;padding:0 10px;color:var(--grey-text)">
      <div class="sub">BEGLEITUNG</div>
      <p>Die gute Nachricht: Sie müssen diese belastende Situation nicht allein bewältigen - erleben Sie Erleichterung, indem Sie sich von mir beraten lassen.</p>
      <p>Als Coach gehe ich ganz individuell auf Ihre Person und auf Ihre persönliche Situation ein.</p>
      <div class="sub" style="margin-top:24px">STÄRKUNG</div>
      <p>Entscheiden Sie sich für einen Weg, der zu Ihnen passt und Sie glücklich macht.</p>
      <p>Finden Sie die Mutterrolle, die es Ihnen ermöglicht, gut für sich zu sorgen und bei sich zu bleiben. Leben Sie so Ihre Bedürfnisse und Interessen im Einklang mit denen Ihrer Familie.</p>
      <div class="sub" style="margin-top:24px">BERATUNG</div>
      <p>Trotz einer Flut an Informationen fühlen sich viele Mütter mit ihren Themen alleine gelassen, hilflos und überfordert.</p>
      <p>Bei mir bleiben Sie nicht allein und ratlos: zusammen finden wir individuelle Antworten auf Ihre ganz persönlichen Fragen.</p>
    </div>
  </div>

  <div class="panel p3">
    <div class="block" style="top:20px;padding:0 14px">
      <div class="h-col">UNSER <span>WEG</span></div><div class="rule"></div>
    </div>
    <div class="block offer" style="top:42px;padding:0 10px 0 14px">
      <p>Gemeinsam können wir Ihre Situation durchleuchten.</p>
      <div class="sub" style="margin:18px 0 30px">MEIN ANGEBOT UMFASST...</div>
      <h4><span class="plus">+</span>Einzelcoaching</h4>
      <p>Sie können wählen: das Coaching kann in meiner Praxis in Neuss oder gern auch bei Ihnen zu Hause stattfinden, allein oder mit Partner, so wie es gerade für Sie am besten passt.</p>
      <h4><span class="plus">+</span>Gruppencoaching</h4>
      <p>Lernen Sie Gleichgesinnte kennen und profitieren Sie in doppelter Hinsicht – nach dem Motto: „Lieber gemeinsam als einsam“.</p>
      <h4><span class="plus">+</span>Telefoncoaching</h4>
      <p>Sie bestimmen Ort und Zeit. Dieses Angebot könnte das Richtige für Sie sein, wenn Sie zeitlich oder örtlich gebunden sind.</p>
    </div>
  </div>

  <div class="band-top"></div>
  <div class="marker" style="left:30px"></div>
  <div class="marker" style="left:273px"></div>
  <div class="marker" style="left:401px"></div>
  <div class="band-bottom"></div>
</section>

</body>
</html>
```